Letterhead and Envelopes design using existing logo. Logo can be found at ridgemontcaldera.example

Use existing logo (attached) and incorporate in letterhead and envelope designs.

Current logo can be viewed at ridgemontcaldera.example the web site reflect various parent and sub companies. Please see attached as well.

Target Market(s)

Other oil and gas operators.

Industry/Entity Type

Oil And Gas

Font styles to use
Sans Serif

Colors

Designer to choose colors to be used in the design.

Requirements
Must have
• Current logo and address
Nice to have
• Modern, contemporary approach yet incorporate existing traditional design.
• After design is selected for Ridgemont Caldera Holdings I will use similar design for Royalties, Exploration, Energy and Farms with different color schemes.

```html
<!DOCTYPE html>
<html lang="en">
<head>
<meta charset="utf-8">
<title>Ridgemont Caldera Holdings – Letterhead</title>
<link rel="stylesheet" href="https://fonts.googleapis.com/css2?family=Open+Sans:wght@400;700&display=swap">
<style>
  :root {
    --paper: #ffffff;
    --brand-green: #6db33f;
    --ink: #1a1a1a;
    --ink-soft: #555555;
    --watermark: #f4f5f5;
  }
  html, body {
    margin: 0;
    padding: 0;
    width: 900px;
    height: 1200px;
    overflow: hidden;
    background: var(--paper);
    font-family: "Open Sans", Arial, sans-serif;
  }
  .letterhead {
    position: relative;
    width: 900px;
    height: 1200px;
    background: var(--paper);
    overflow: hidden;
  }
  .brand-mark {
    position: absolute;
    top: 46px;
    left: 0;
    width: 100%;
    display: flex;
    flex-direction: column;
    align-items: center;
    gap: 10px;
  }
  .brand-dot {
    width: 58px;
    height: 58px;
    border-radius: 50%;
    background: var(--brand-green);
  }
  .brand-name {
    font-size: 15px;
    font-weight: 700;
    color: var(--ink);
    letter-spacing: 0.5px;
  }
  .watermark-disc {
    position: absolute;
    top: 300px;
    right: -150px;
    width: 620px;
    height: 620px;
    border-radius: 50%;
    background: var(--watermark);
  }
  .footer {
    position: absolute;
    bottom: 60px;
    left: 0;
    width: 100%;
    text-align: center;
  }
  .footer-company {
    margin: 0 0 4px;
    font-size: 16px;
    font-weight: 700;
    color: var(--brand-green);
  }
  .footer-contact {
    margin: 0;
    font-size: 12px;
    color: var(--ink-soft);
  }
  .footer-band {
    position: absolute;
    bottom: 18px;
    left: 0;
    width: 900px;
    height: 22px;
  }
</style>
</head>
<body>
  <main class="letterhead">
    <header class="brand-mark">
      <span class="brand-dot"></span>
      <span class="brand-name">Ridgemont Caldera Holdings</span>
    </header>

    <div class="watermark-disc" aria-hidden="true"></div>

    <footer class="footer">
      <p class="footer-company">Ridgemont Caldera Holdings, LLC</p>
      <p class="footer-contact">PO Box 410 Lakefield, Montana 59001 &nbsp;•&nbsp; (555) 010-2468 &nbsp;•&nbsp; www.ridgemontcaldera.example</p>
    </footer>

    <svg class="footer-band" viewBox="0 0 900 22" aria-hidden="true">
      <rect x="0" y="8" width="900" height="8" fill="var(--brand-green)"/>
      <polygon points="560,0 900,0 900,22 540,22" fill="var(--ink)"/>
    </svg>
  </main>
</body>
</html>
```